Movie poster for short film: TINFOIL

We need a creative, artistic, stylized poster design for our short film TINFOIL. We would like to see designs with graphics and bold colors more than photographs. The photographs we are posting are more for reference- you do not have to use them in the poster! We are looking for something clean and simple. The film is a drama so please don't make it funny. The mood of the film is thoughtful and introspective. Name of film should be in all caps. Things to include in the poster:
Name of film: TINFOIL
Velvet Harbor Pictures
Starring Marisa Calloway

Here is a brief plot synopsis: TINFOIL follows one night in the life of a rebellious young woman who breaks into a diner after hours with a can of spray paint. Her intentions change after she ends up discovering what's left of a love story.

The movie is somewhat experimental, set to music for part of it with no dialog. The whole movie takes place in an old fashioned diner.

Target Market(s)

Film festival attendees between the ages of 20-50

Industry/Entity Type

Movie

Font styles to use
Sans Serif

Requirements
Must have
• See project description above- also the film is somewhat dark in nature so please don't make it too 'happy' looking.

```html
<!DOCTYPE html>
<html lang="en">
<head>
<meta charset="utf-8">
<title>TINFOIL – Poster</title>
<link rel="stylesheet" href="https://fonts.googleapis.com/css2?family=Bebas+Neue&display=swap">
<style>
  :root {
    --paper: #ffffff;
    --ink: #000000;
    --coral: #f48c70;
    --rust: #9b5946;
  }
  html, body {
    margin: 0;
    padding: 0;
    overflow: hidden;
    background: var(--paper);
  }
  .poster {
    display: block;
    width: 960px;
    height: 1200px;
    background: var(--paper);
  }
  .poster-type {
    font-family: "Bebas Neue", "Oswald", sans-serif;
  }
  .studio-name {
    font-size: 47px;
    fill: var(--ink);
  }
  .film-title {
    font-size: 330px;
  }
  .film-title--ink { fill: var(--ink); }
  .film-title--rust { fill: var(--rust); }
  .billing {
    font-size: 60px;
    fill: var(--ink);
  }
  .coral-blob { fill: var(--coral); }
  .splash-stop-ink { stop-color: var(--ink); }
  .splash-stop-rust { stop-color: var(--rust); }
</style>
</head>
<body>
<svg class="poster" viewBox="0 0 1152 1440" xmlns="http://www.w3.org/2000/svg">
  <defs>
    <path id="blob-shape" d="M600,250 C760,250 900,280 960,320 C1010,360 1025,440 1020,540 C1010,680 960,780 880,840 C810,890 720,892 620,885 C480,875 340,840 300,730 C275,660 290,560 320,440 C350,320 450,250 600,250 Z"/>
    <clipPath id="blob-clip">
      <use href="#blob-shape"/>
    </clipPath>
    <radialGradient id="splash-ink">
      <stop offset="0" class="splash-stop-ink" stop-opacity="1"/>
      <stop offset="0.55" class="splash-stop-ink" stop-opacity="0.9"/>
      <stop offset="1" class="splash-stop-ink" stop-opacity="0"/>
    </radialGradient>
    <radialGradient id="splash-rust">
      <stop offset="0" class="splash-stop-rust" stop-opacity="1"/>
      <stop offset="0.55" class="splash-stop-rust" stop-opacity="0.9"/>
      <stop offset="1" class="splash-stop-rust" stop-opacity="0"/>
    </radialGradient>
  </defs>

  <!-- background shape -->
  <use href="#blob-shape" class="coral-blob"/>

  <!-- ink splash areas -->
  <g role="img" aria-label="Black ink splatter, upper left">
    <ellipse cx="325" cy="210" rx="135" ry="135" fill="url(#splash-ink)"/>
  </g>
  <g role="img" aria-label="Rust ink splatter on the coral shape, upper right">
    <ellipse cx="925" cy="330" rx="72" ry="80" fill="url(#splash-rust)"/>
  </g>
  <g role="img" aria-label="Black ink splatter, lower right">
    <ellipse cx="1015" cy="905" rx="125" ry="140" fill="url(#splash-ink)"/>
  </g>
  <g role="img" aria-label="Black ink splatter, lower left">
    <ellipse cx="185" cy="1125" rx="145" ry="130" fill="url(#splash-ink)"/>
  </g>

  <!-- studio -->
  <text class="poster-type studio-name" x="528" y="184">VELVET HARBOR PICTURES</text>

  <!-- title: ink, with rust where it crosses the coral shape -->
  <text class="poster-type film-title film-title--ink" x="95" y="670">TINFOIL</text>
  <g clip-path="url(#blob-clip)" aria-hidden="true">
    <text class="poster-type film-title film-title--rust" x="95" y="670">TINFOIL</text>
  </g>

  <!-- billing -->
  <text class="poster-type billing" x="288" y="1057">STARRING MARISA CALLOWAY</text>
</svg>
</body>
</html>
```